Whitepaper: 7 Keys to Achieving Success of Your RTLS Initiative

Create a graphical layout for a whitepaper that would include 7 illustrations matching each subject line. Colors aligned with Boundless Stride branding guide (attached)
Updates

Just to summarize, I would need graphics/illustrations for 7 bullet points - Key #1: Set Measurements for Success Key #2: Establish a Clear Roadmap Key #3: Don’t Use Pilots (small try out of software) Key #4: Plan for the Future, from the Start Key #5: Think about RTLS as an Initiative, not a Project Key #6: Nurture the Change Key #7: Show Successes, Early

I would expect about 2-3 illustrations per page. Format - US size 8.5x11. PDF file, but would like to have the ability to edit text if needed. Thank you for your interest. Colors don't need to match the branding. It is a healthcare whitepaper so it could be blue and green.

Project Deadline Extended
Reason: Some of you have asked for a time extension.

```html
<!DOCTYPE html>
<html lang="en">
<head>
<meta charset="utf-8">
<title>7 Keys to Achieving Success of Your RTLS Initiative – Key #7</title>
<link rel="stylesheet" href="https://fonts.googleapis.com/css2?family=Nunito:wght@700;800&family=Nunito+Sans:ital,wght@0,400;0,600;0,700;1,400&display=swap">
<style>
  :root {
    --backdrop: #d9d9d9;
    --paper: #ffffff;
    --coral: #f26966;
    --coral-soft: #f8b3b0;
    --ink: #2f3340;
    --body: #4a4d57;
    --rule: #d4d4d8;
    --footer: #3d404b;
    --white: #ffffff;
  }
  * { box-sizing: border-box; margin: 0; padding: 0; }
  html, body {
    width: 1200px; height: 793px; overflow: hidden;
    background: var(--backdrop);
    font-family: "Nunito Sans", sans-serif;
  }
  .page {
    position: absolute; left: 344px; top: 64px;
    width: 520px; height: 670px;
    background: var(--paper);
    overflow: hidden;
  }
  .brand {
    position: absolute; left: 66px; top: 44px;
    font-family: "Nunito Sans", sans-serif;
    font-weight: 600; font-size: 17px; color: var(--ink);
    letter-spacing: -0.2px;
  }
  .running-head {
    position: absolute; left: 166px; right: 67px; top: 48px;
    border-bottom: 1px solid var(--rule);
    padding-bottom: 5px;
    text-align: right;
    font-size: 6.4px; font-weight: 700; color: var(--ink);
  }
  .key-illustration {
    position: absolute; left: 66px; top: 104px;
    width: 70px; height: 68px;
    border-radius: 10px;
    background: linear-gradient(160deg, var(--coral-soft), var(--coral));
    opacity: 0.85;
  }
  .key-badge {
    position: absolute; left: 165px; top: 116px;
    height: 27px; padding: 0 10px;
    border-radius: 14px;
    background: var(--coral); color: var(--white);
    font-family: "Nunito", sans-serif; font-weight: 700; font-size: 13.5px;
    line-height: 27px;
  }
  .key-title {
    position: absolute; left: 165px; top: 149px;
    font-family: "Nunito", sans-serif; font-weight: 800; font-size: 17px;
    color: var(--ink);
  }
  .body-copy {
    position: absolute; left: 66px; top: 185px; width: 392px;
    font-size: 9.6px; line-height: 17.3px; color: var(--body);
  }
  .body-copy p + p { margin-top: 17px; }
  .author-band {
    position: absolute; left: 38px; top: 434px;
    width: 443px; height: 138px;
    border-radius: 69px;
    background: var(--coral);
  }
  .author-photo {
    position: absolute; left: 26px; top: 27px;
    width: 84px; height: 84px; border-radius: 50%;
    border: 3px solid var(--white);
    background: radial-gradient(circle at 50% 40%, #c9a48f, #6f6a6a 70%, #3b3b40);
  }
  .author-name {
    position: absolute; left: 127px; top: 10px;
    font-family: "Nunito", sans-serif; font-weight: 700; font-size: 12.4px;
    color: var(--white);
  }
  .author-bio {
    position: absolute; left: 127px; top: 29px; width: 290px;
    font-style: italic; font-size: 8.3px; line-height: 12.2px;
    color: var(--white);
  }
  .page-number {
    position: absolute; left: 405px; top: 593px;
    width: 48px; height: 48px; border-radius: 50%;
    background: var(--coral); color: var(--white);
    font-family: "Nunito", sans-serif; font-weight: 800; font-size: 17px;
    line-height: 48px; text-align: center;
    z-index: 2;
  }
  .page-footer {
    position: absolute; left: 0; bottom: 0; width: 100%; height: 48px;
    background: var(--footer); color: var(--white);
    padding: 13px 0 0 66px;
    font-size: 7.8px; line-height: 12.6px;
  }
</style>
</head>
<body>
  <article class="page">
    <header>
      <div class="brand">Boundless Stride</div>
      <div class="running-head">7 Keys to Achieving Success of Your RTLS Initiative</div>
    </header>

    <div class="key-illustration" role="img" aria-label="Trophy illustration with a star, representing early successes"></div>
    <div class="key-badge">Key #7:</div>
    <h2 class="key-title">Show Successes, Early</h2>

    <section class="body-copy">
      <p>To create excitement around RTLS initiative, you must demonstrate the value it brings to the organization. However, don’t only focus on hard dollar savings, such as avoided rentals or purchases. Ask your nurses how much time the system saves them, how much happier they are at work. And don’t wait for the fiscal year to end to report these results, share success stories often and early to increase the system adoption and create momentum for your initiative.</p>
      <p>As you can see, ensuring the success of your RTLS initiative is not an easy task. It requires executive commitment, dedicated resources, and adoption by the staff on the floor – only then you can provide the value to your patients and staff and achieve tangible ROI to your organization.</p>
    </section>

    <aside class="author-band">
      <div class="author-photo" role="img" aria-label="Portrait photo of the author"></div>
      <h3 class="author-name">About Dr. Martin Hale</h3>
      <p class="author-bio">Dr. Hale is a medical informaticist and emergency medicine physician. He has been part of the design, implementation, optimization and value realization process for EHR systems, principally Cirrus, through 28 hospitals and hundreds of ambulatory clinics across 3 major health care systems, both academic and non-academic. He also has a significant interest and experience with leveraging Real-Time Location technologies in the healthcare environment.</p>
    </aside>

    <div class="page-number">04</div>
    <footer class="page-footer">
      © 2017 BOUNDLESS STRIDE, INC. ALL RIGHTS RESERVED.<br>
      www.boundlessstride.net
    </footer>
  </article>
</body>
</html>
```